electrical contractor business card for professional modern company

I need a business card design for an electrical contractors business. I do all kinds of electricical work from new homes, air conditioning, data and communications. I have a logo design i want on it and have a good idea in my head of what i want it to look like. I like simple yet bold and professional looking. All black background is a must

Target Market(s)

Anyone needing electrical work done

Industry/Entity Type

Electrical

Contact Information for Business Card

company name- KTW Electrical and Data
person name-martin pellowe
phone number- 0418 362 927
website-ktwelec.example.com.au

Font styles to use
Sans Serif

Requirements
Must have
• email
• website
• logo
• name
• phone number
• list of work i do:
• -electrical
• -air-conditioning
• -data/communications
• -cctv/security
• -domestic/commercial/industrial
• -24hr emergency breakdown repair
Nice to have
• i would like the logo on the front side in the centre taking up most of the card with black background.
• on the rear i want the list of work i do with company info i.e. email, website, my name, phone number. rear of card also black background with orange writing to match the orange in the logo

```html
<!DOCTYPE html>
<html lang="en">
<head>
<meta charset="utf-8">
<title>KTW Electrical and Data – Business Card</title>
<link rel="stylesheet" href="https://fonts.googleapis.com/css2?family=Exo+2:wght@400;600&display=swap">
<style>
  :root {
    --page: #f4f4f4;
    --card: #0b0b0b;
    --orange: #f26a21;
    --text: #d9d9d9;
    --muted: #a6a6a6;
  }
  * { box-sizing: border-box; margin: 0; padding: 0; }
  html, body {
    width: 1200px; height: 800px; overflow: hidden;
    background: var(--page);
    font-family: "Exo 2", "Segoe UI", sans-serif;
  }
  .sheet {
    width: 1200px; height: 800px;
    display: flex; align-items: center; justify-content: center; gap: 60px;
  }
  .card {
    width: 540px; height: 310px;
    border-radius: 22px;
    background: var(--card);
    position: relative; overflow: hidden;
    box-shadow: 0 14px 30px rgba(0,0,0,.28);
  }

  /* Back: contact details */
  .card--details {
    background: radial-gradient(ellipse at 40% 35%, #2a2a2a 0%, #141414 55%, #080808 100%);
  }
  .texture {
    position: absolute; inset: 0;
    background: linear-gradient(160deg, rgba(255,255,255,.05), rgba(0,0,0,0) 60%);
  }
  .details-top {
    position: absolute; left: 32px; right: 24px; top: 38px; height: 170px;
    display: flex; align-items: center;
  }
  .brand-small {
    width: 158px;
    color: var(--text); font-weight: 600; font-size: 19px; line-height: 1.25;
  }
  .divider {
    flex: none; width: 2px; height: 150px; background: var(--orange); margin: 0 22px 0 10px;
  }
  .contact { display: flex; flex-direction: column; gap: 9px; }
  .contact-name {
    color: var(--orange); font-weight: 600; font-size: 21px;
    letter-spacing: .14em; text-transform: uppercase; margin-bottom: 4px;
    white-space: nowrap;
  }
  .contact-line {
    display: flex; align-items: center; gap: 8px;
    color: var(--text); font-size: 14px; font-weight: 400;
    white-space: nowrap;
  }
  .contact-line svg { width: 13px; height: 13px; flex: none; }
  .services {
    position: absolute; left: 32px; right: 24px; bottom: 32px;
    color: var(--muted); font-size: 9.5px; letter-spacing: .1em;
    text-transform: uppercase; line-height: 1.9;
  }
  .services span { display: block; white-space: nowrap; }

  /* Front: brand */
  .card--brand {
    display: flex; align-items: center; justify-content: center;
  }
  .brand-large-name {
    color: var(--text); font-weight: 600; font-size: 40px; line-height: 1.15;
    text-align: center;
  }
</style>
</head>
<body>
<main class="sheet">

  <article class="card card--details">
    <div class="texture" role="img" aria-label="Dark perforated metal texture background"></div>

    <div class="details-top">
      <div class="brand-small">KTW Electrical<br>and Data</div>
      <span class="divider"></span>
      <div class="contact">
        <h1 class="contact-name">Martin Pellowe</h1>
        <p class="contact-line">
          <svg viewBox="0 0 14 14" aria-hidden="true"><rect x="3" y="1" width="8" height="12" rx="1.5" fill="none" stroke="#d9d9d9" stroke-width="1.4"/></svg>
          0418 362 927
        </p>
        <p class="contact-line">
          <svg viewBox="0 0 14 14" aria-hidden="true"><rect x="1" y="3" width="12" height="8" fill="none" stroke="#d9d9d9" stroke-width="1.3"/><path d="M1 3l6 5 6-5" fill="none" stroke="#d9d9d9" stroke-width="1.3"/></svg>
          Email@
        </p>
        <p class="contact-line">
          <svg viewBox="0 0 14 14" aria-hidden="true"><circle cx="7" cy="7" r="6" fill="none" stroke="#d9d9d9" stroke-width="1.3"/><ellipse cx="7" cy="7" rx="2.6" ry="6" fill="none" stroke="#d9d9d9" stroke-width="1"/><path d="M1 7h12" stroke="#d9d9d9" stroke-width="1"/></svg>
          website-ktwelec.example.com.au
        </p>
      </div>
    </div>

    <p class="services">
      <span>Electrical | Air-Conditioning | Data/Communications | CCTV/Security</span>
      <span>Domestic/Commercial/Industrial | 24hr Emergency Breakdown Repair</span>
    </p>
  </article>

  <article class="card card--brand">
    <span class="brand-large-name">KTW Electrical<br>and Data</span>
  </article>

</main>
</body>
</html>
```